New Business Cards for Torvin Group

We need a new Business Card to compliment our new logo. We are a vibrant design, manufacture and install business providing recreation areas, public parks and Municipal spaces. We want business cards that are classy, modern and clean.

We have recently changed our logo, and are celebrating our 40th anniversary. We want business cards with a new modern design to reflect our status.

Target Market(s)

Customers

Contact Information for Business Card

We need all the details of our 3 offices as per the business card attached. Please disregard the old logo on the business card, the other three files show our new logo.

Requirements
Must have
• All info as per attached business card but with new logo.
Nice to have

```html
<!DOCTYPE html>
<html lang="en">
<head>
<meta charset="utf-8">
<title>Torvin Group – Business Card</title>
<link href="https://fonts.googleapis.com/css2?family=Open+Sans:wght@400;600;700&display=swap" rel="stylesheet">
<style>
  :root {
    --red: #e0313a;
    --red-soft: #f3b7ba;
    --charcoal: #45464a;
    --ink: #1c1c1c;
    --paper: #fbfbfb;
    --backdrop: #e9e7e3;
    --watermark: #ececec;
  }
  * { margin: 0; padding: 0; box-sizing: border-box; }
  html, body { width: 1200px; height: 1023px; overflow: hidden; }
  body {
    background: var(--backdrop);
    font-family: "Open Sans", sans-serif;
    color: var(--ink);
    position: relative;
  }
  .card {
    position: absolute;
    left: 100px; top: 226px;
    width: 1000px; height: 571px;
    background: var(--paper);
    box-shadow: 0 18px 40px rgba(0,0,0,.18);
    overflow: hidden;
  }
  .watermark {
    position: absolute; left: 470px; top: 150px;
    display: flex; align-items: center; gap: 24px;
    color: var(--watermark);
    font-size: 92px; font-weight: 700; letter-spacing: 2px;
  }
  .watermark .mark-circle {
    width: 170px; height: 170px; border-radius: 50%;
    border: 22px solid var(--watermark);
  }
  .brand {
    position: absolute; left: 44px; top: 206px;
    display: flex; align-items: center; gap: 16px;
    color: var(--charcoal);
    font-size: 44px; font-weight: 700; letter-spacing: .5px;
  }
  .brand .mark-circle {
    width: 80px; height: 80px; border-radius: 50%;
    background: var(--red);
  }
  .person {
    position: absolute; left: 590px; top: 40px; width: 370px;
  }
  .person-name {
    color: var(--red); font-size: 32px; font-weight: 700;
    letter-spacing: .5px; line-height: 1.1;
    padding-bottom: 6px; border-bottom: 2px solid var(--red);
  }
  .person-title {
    color: var(--red); font-size: 16px; font-weight: 600;
    margin-top: 6px; padding-bottom: 6px;
    border-bottom: 2px solid var(--red); width: 270px;
  }
  .contact-list { list-style: none; margin-top: 10px; }
  .contact-list li {
    display: flex; align-items: center; gap: 10px;
    font-size: 17px; line-height: 30px;
  }
  .contact-list svg { width: 20px; height: 20px; flex: none; }
  .offices {
    position: absolute; left: 40px; top: 330px; right: 40px;
    display: flex; gap: 60px;
  }
  .office { width: 280px; }
  .office-name {
    font-size: 18px; font-weight: 700;
    padding-bottom: 4px; border-bottom: 2px solid var(--red);
  }
  .footer-strip { position: absolute; left: 0; right: 0; bottom: 0; height: 64px; }
  .footer-strip .band-red {
    position: absolute; bottom: 0; height: 44px; background: var(--red);
  }
  .footer-strip .band-left { left: 0; width: 300px; }
  .footer-strip .band-right { right: 0; width: 190px; }
  .footer-strip .band-web {
    position: absolute; left: 300px; width: 510px; bottom: 0; height: 64px;
    background: var(--charcoal); color: #fff;
    font-size: 19px; font-weight: 700;
    display: flex; align-items: center; justify-content: center;
  }
</style>
</head>
<body>
<svg width="0" height="0" style="position:absolute" aria-hidden="true">
  <defs>
    <symbol id="icon-home" viewBox="0 0 20 20">
      <path d="M10 2 L19 10 H16 V18 H4 V10 H1 Z" fill="#1c1c1c"/>
      <circle cx="10" cy="12" r="2.6" fill="#fff"/>
    </symbol>
    <symbol id="icon-phone" viewBox="0 0 20 20">
      <circle cx="10" cy="10" r="8.5" fill="none" stroke="#1c1c1c" stroke-width="1.8"/>
      <path d="M7 6 C6 9 9 13 13 14 L14 12.5 L12 11.5 L11 12.3 C9.8 11.6 8.6 10.3 8 9 L8.8 8 L8 6 Z" fill="#1c1c1c"/>
    </symbol>
    <symbol id="icon-fax" viewBox="0 0 20 20">
      <circle cx="10" cy="10" r="9.5" fill="#1c1c1c"/>
      <rect x="5" y="7" width="10" height="7" rx="1" fill="#fff"/>
      <rect x="7" y="5" width="6" height="3" fill="#fff"/>
      <rect x="7" y="10" width="6" height="1.4" fill="#1c1c1c"/>
    </symbol>
    <symbol id="icon-mail" viewBox="0 0 20 20">
      <rect x="1" y="2" width="18" height="16" fill="#1c1c1c"/>
      <path d="M4 15 V6 L10 11 L16 6 V15" fill="none" stroke="#fff" stroke-width="1.8"/>
    </symbol>
  </defs>
</svg>

<main class="card">
  <div class="watermark" aria-hidden="true">
    <span class="mark-circle"></span><span>TORVIN</span>
  </div>

  <div class="brand">
    <span class="mark-circle"></span><span>Torvin Group</span>
  </div>

  <section class="person">
    <h1 class="person-name">RAMI VOSTEL</h1>
    <p class="person-title">MANAGING PARTNER</p>
    <ul class="contact-list">
      <li><svg><use href="#icon-phone"/></svg>+971 (0)50 555 0142</li>
      <li><svg><use href="#icon-mail"/></svg>rami@torvingroup.com</li>
    </ul>
  </section>

  <section class="offices">
    <div class="office">
      <h2 class="office-name">Head Office</h2>
      <ul class="contact-list">
        <li><svg><use href="#icon-home"/></svg>41208 Abu Dhabi, U.A.E.</li>
        <li><svg><use href="#icon-phone"/></svg>+971 (0)2 5550184</li>
        <li><svg><use href="#icon-fax"/></svg>+971 (0)2 5550183</li>
        <li><svg><use href="#icon-mail"/></svg>sales@torvingroup.com</li>
      </ul>
    </div>
    <div class="office">
      <h2 class="office-name">Dubai Office</h2>
      <ul class="contact-list">
        <li><svg><use href="#icon-home"/></svg>517340 Dubai, U.A.E.</li>
        <li><svg><use href="#icon-phone"/></svg>+971 (0)4 5550691</li>
        <li><svg><use href="#icon-fax"/></svg>+971 (0)4 5550769</li>
        <li><svg><use href="#icon-mail"/></svg>sales@torvingroup.com</li>
      </ul>
    </div>
    <div class="office">
      <h2 class="office-name">Qatar Office</h2>
      <ul class="contact-list">
        <li><svg><use href="#icon-home"/></svg>27093 Doha, Qatar</li>
        <li><svg><use href="#icon-phone"/></svg>+974 55502195</li>
        <li><svg><use href="#icon-fax"/></svg>+974 55509260</li>
        <li><svg><use href="#icon-mail"/></svg>sales@torvingroup.com</li>
      </ul>
    </div>
  </section>

  <footer class="footer-strip">
    <span class="band-red band-left"></span>
    <span class="band-web">www.torvingroup.com</span>
    <span class="band-red band-right"></span>
  </footer>
</main>
</body>
</html>
```